Small holiday retreat needs new Internet launch

"The Evolution from a Ruin into a Holiday Retreat.
My wife and I rebuilt a small farm in a remote village into a little holiday retreat. Though close to the Baltic Sea, we want to attract people with the desire to spend some days in a secluded place. Though remote it offers some luxury - and time ticks slower.
This summer was our third season and we want to adapt our Internet pages. Look at our business card - we want to keep this style.
It should be a bit mystic and should not attract the bargain hunter.
We realized that in summer our name "Wiesenkrone" (ie sunny hill) does not fit for the dark part of the year - then it is more like "Glimmering Moors".
We have a guesthouse (the former stable) and two tiny houses. Additionally, we have lavatory with sauna in the rebuilt barn and a fitness room.
On our farm live a few animals (dog, cats, chicken, bees) + wild visitors.
Our current home page is www.wiesenkrone-example.net
A few pictures are on Mapvista Atlas and I can share more in Cloudkeep Vault.
The final homepage should also offer translations into English, French, Dutch.
Better and consistent fonts.
No "galery" but more "four seasons".

Target Market(s)

Individual travellers - not just from Germany!

Industry/Entity Type

Tourism

Coding

Coded - Design and coding required

Number of Pages Required

4 page

Font styles to use
Script

Colors
FFC000
F8CF3A
FAE287
FDF2CF
FEFAEE

Requirements
Must have
• A "mystic" and romantic appearance.
Nice to have
• See my comments.

```html
<!DOCTYPE html>
<html lang="en">
<head>
<meta charset="utf-8">
<title>Wiesenkrone – Holiday Retreat</title>
<link href="https://fonts.googleapis.com/css2?family=Cinzel:wght@400;500&family=Great+Vibes&family=Poppins:ital,wght@0,300;0,400;0,500;0,600;1,300&display=swap" rel="stylesheet">
<style>
:root{
  --gold:#E9B53A;
  --gold-deep:#D89A22;
  --gold-light:#F8CF3A;
  --cream:#FDF2CF;
  --ivory:#FEFAEE;
  --ink:#2b2b2b;
  --muted:#555;
  --grey-bg:#EFEFEF;
  --brown-top:#54432b;
  --brown-bottom:#2c2216;
  --dark-btn:#2a2620;
}
*{box-sizing:border-box;margin:0;padding:0}
html,body{width:1200px;height:5344px;overflow:hidden}
body{position:relative;background:#fff;font-family:'Poppins',sans-serif;color:var(--ink)}
.abs{position:absolute}
.script{font-family:'Great Vibes',cursive;color:var(--gold);font-weight:400}
.caps{font-family:'Cinzel',serif;font-weight:400;letter-spacing:1px}
.photo{position:absolute;border-radius:4px}

/* header */
.topbar{left:0;top:0;width:1200px;height:100px;background:#fff}
.lang{left:210px;top:36px;width:66px;height:22px;border-radius:11px;background:var(--gold);color:#fff;font-size:10px;display:flex;align-items:center;gap:5px;padding-left:6px}
.lang .flag{width:14px;height:14px;border-radius:50%;background:#fff;border:3px solid #c23b3b}
.brand{left:500px;top:22px;width:200px;height:56px;display:flex;align-items:center;justify-content:center;gap:8px;font-size:18px;font-weight:500;color:var(--gold)}
.brand .dot{width:34px;height:34px;border-radius:50%;background:var(--gold)}
.phone{left:852px;top:38px;font-size:12px;color:var(--gold-deep);display:flex;gap:6px;align-items:center}

/* hero */
.hero{left:0;top:100px;width:1200px;height:800px;background:linear-gradient(180deg,#4d6591 0%,#7a90b0 22%,#8aa088 48%,#5e7a3a 70%,#4d6a2c 100%)}
.nav{left:0;top:100px;width:1200px;height:76px;font-size:13px;color:#fff}
.nav a{position:absolute;top:0;height:76px;line-height:76px;color:#fff;text-decoration:none}
.nav a.active{background:var(--gold);padding:0 14px}
.hero-title{left:0;top:280px;width:1200px;text-align:center;font-family:'Great Vibes',cursive;font-weight:400;font-size:112px;color:#fff;line-height:1}
.hero-sub{left:0;top:440px;width:1200px;text-align:center;font-size:17px;font-style:italic;font-weight:300;color:#fff;line-height:34px}
.booking{left:210px;top:525px;width:780px;height:96px;background:var(--gold);border-radius:4px;display:flex;align-items:center;gap:16px;padding:0 20px}
.field{height:46px;width:188px;background:#fff;border-radius:3px;font-size:12px;color:#444;display:flex;align-items:center;justify-content:space-between;padding:0 12px}
.field i{width:12px;height:12px;border:1.5px solid var(--gold);border-radius:2px;display:block}
.btn-search{height:46px;width:118px;background:var(--dark-btn);color:#fff;font-size:13px;border-radius:3px;display:flex;align-items:center;justify-content:center}
.hero-wave{left:0;top:680px;width:1200px;height:230px}

/* welcome */
.sec-script{left:0;width:1200px;text-align:center;font-size:42px}
.sec-title{left:0;width:1200px;text-align:center;font-size:34px;line-height:50px;color:var(--ink)}
.body-copy{color:#333}
.intro{left:590px;top:1152px;width:405px;font-size:11.5px;line-height:24.5px}
.aside{left:778px;top:1350px;width:218px;font-size:10.5px;line-height:24px}
.rating{left:370px;top:1350px;width:208px;height:190px;background:var(--ivory);text-align:center}
.rating .mini{width:120px;height:30px;margin:16px auto 0;display:flex;align-items:center;justify-content:center;gap:5px;font-size:10px;color:var(--gold)}
.rating .mini span{width:14px;height:14px;border-radius:50%;background:var(--gold)}
.rating .score{font-size:44px;font-weight:600;color:var(--gold);line-height:60px}
.rating .stars{color:var(--gold);font-size:11px;letter-spacing:3px}
.rating .cta{display:inline-block;margin-top:12px;background:#1e1b16;color:#fff;font-size:11px;padding:7px 16px;border-radius:3px}
.signoff{left:778px;top:1480px;font-family:'Cinzel',serif;font-size:10.5px;letter-spacing:.3px}
.signature{left:778px;top:1496px;font-family:'Great Vibes',cursive;font-size:30px;color:#222}

/* domicile */
.domicile{left:0;top:1648px;width:1200px;height:900px;background:var(--grey-bg)}
.card{position:absolute;width:378px;height:302px;border-radius:6px;overflow:hidden}
.card .glass{position:absolute;left:30px;width:170px;background:rgba(255,255,255,.78);border-radius:6px;padding:16px 14px}
.card h3{font-family:'Cinzel',serif;font-weight:400;font-size:17px;line-height:24px;color:#333;letter-spacing:.5px}
.card p{font-size:10px;line-height:20px;color:#444;margin-top:6px}
.card .more{display:inline-block;margin-top:8px;border:1px solid #333;border-radius:3px;font-size:10px;padding:3px 8px}

/* features */
.features{left:0;top:2548px;width:1200px;height:482px;background:linear-gradient(180deg,var(--gold) 0%,var(--gold-deep) 100%)}
.feat{position:absolute;top:2703px;width:113px;height:116px;background:#fff;border-radius:4px;text-align:center;padding-top:34px}
.feat svg{width:26px;height:22px}
.feat div{font-family:'Cinzel',serif;font-size:11px;color:#333;margin-top:8px}
.video{left:210px;top:2890px;width:780px;height:398px;border:4px solid #fff;border-radius:6px;background:linear-gradient(180deg,#6a8a40 0%,#7e9a4a 45%,#5f7e34 100%);box-shadow:0 8px 22px rgba(0,0,0,.18)}
.play{left:548px;top:3046px;width:104px;height:104px;border-radius:50%;background:rgba(255,255,255,.55);display:flex;align-items:center;justify-content:center}
.play span{width:70px;height:70px;border-radius:50%;background:#fff;display:flex;align-items:center;justify-content:center}

/* seasons */
.tabs{left:210px;top:3495px;width:780px;height:48px;display:flex;gap:4px}
.tabs div{flex:1;background:#f1f1f1;font-family:'Cinzel',serif;font-size:22px;display:flex;align-items:center;justify-content:center;color:#333}
.tabs div.on{background:var(--gold)}

/* map & footer */
.map{left:0;top:4300px;width:1200px;height:640px;background:linear-gradient(135deg,#e8ecef 0%,#dfe6e0 40%,#aacbe6 60%,#e7eaea 100%)}
.zoom{left:1132px;top:4682px;width:40px;height:96px;background:#fff;box-shadow:0 1px 4px rgba(0,0,0,.25);font-size:26px;color:#666;text-align:center;line-height:48px}
.footer-wave{left:0;top:4720px;width:1200px;height:240px}
.footer{left:0;top:4900px;width:1200px;height:420px;background:linear-gradient(180deg,var(--brown-top) 0%,var(--brown-bottom) 100%)}
.foot-brand{left:500px;top:4922px;width:200px;height:60px;display:flex;align-items:center;justify-content:center;gap:8px;font-size:20px;font-weight:500;color:var(--gold)}
.foot-brand .dot{width:36px;height:36px;border-radius:50%;background:var(--gold)}
.foot-h{font-family:'Cinzel',serif;font-size:22px;color:#fff;top:5012px}
.foot-links{left:210px;top:5056px;font-size:12px;line-height:35px;color:#fff}
.write{left:430px;top:5058px;font-size:12px;color:#fff;line-height:20px}
.write .row{display:flex;gap:8px;margin-bottom:14px}
.write .gold{color:var(--gold)}
.input{position:absolute;border:1px solid rgba(255,255,255,.3);background:rgba(255,255,255,.06);font-size:9px;color:rgba(255,255,255,.7);padding:6px 8px}
.send{left:670px;top:5248px;width:320px;height:28px;background:var(--gold);color:#fff;font-size:11px;font-weight:600;display:flex;align-items:center;justify-content:center}
.copy{left:0;top:5314px;width:1200px;height:30px;background:var(--gold);font-size:11px;color:#4a3a20;display:flex;align-items:center;justify-content:center}
</style>
</head>
<body>

<!-- Header -->
<div class="abs topbar"></div>
<div class="abs lang"><span class="flag"></span>ENG ▾</div>
<div class="abs brand"><span class="dot"></span>Wiesenkrone</div>
<div class="abs phone">
  <svg width="12" height="12" viewBox="0 0 24 24"><path fill="#D89A22" d="M6.6 10.8a15.1 15.1 0 0 0 6.6 6.6l2.2-2.2a1 1 0 0 1 1-.25 11.4 11.4 0 0 0 3.6.57 1 1 0 0 1 1 1V20a1 1 0 0 1-1 1A17 17 0 0 1 3 4a1 1 0 0 1 1-1h3.5a1 1 0 0 1 1 1c0 1.25.2 2.45.57 3.57a1 1 0 0 1-.25 1z"/></svg>
  +49 000 555 014 20</div>

<!-- Hero -->
<div class="abs hero" role="img" aria-label="Photo of the tiny houses in a green meadow under an evening sky"></div>
<nav class="abs nav">
  <a class="active" style="left:212px">Home</a>
  <a style="left:318px">About Us</a>
  <a style="left:443px">Accommodation</a>
  <a style="left:622px">Booking &amp; Calendar</a>
  <a style="left:820px">Gallery</a>
  <a style="left:935px">Contact</a>
</nav>
<h1 class="abs hero-title">Spend Your Holidays</h1>
<p class="abs hero-sub">Get to know our accommodations and book directly with us in a relaxed manner.<br>You can find the current occupancy calendar further down on this page.</p>
<div class="abs booking">
  <div class="field">Check - In Date <i></i></div>
  <div class="field">Check - In Date <i></i></div>
  <div class="field">Person <span style="font-size:9px">▾</span></div>
  <div class="btn-search">Search</div>
</div>
<svg class="abs hero-wave" viewBox="0 0 1200 230" preserveAspectRatio="none">
  <path d="M0 30 C260 150 520 170 760 140 C940 118 1080 80 1200 40 L1200 230 L0 230 Z" fill="#E9B53A"/>
  <path d="M0 60 C250 190 520 200 760 172 C940 150 1080 112 1200 78 L1200 230 L0 230 Z" fill="#fff"/>
</svg>

<!-- Welcome -->
<div class="abs sec-script script" style="top:950px">Welcome to the</div>
<h2 class="abs sec-title caps" style="top:1005px">Wiesenkrone in beautiful<br>Lindental</h2>
<div class="photo" style="left:210px;top:1130px;width:367px;height:220px;background:linear-gradient(135deg,#8a5a1e,#d6a443 55%,#6e4418)" role="img" aria-label="Photo of a warm-lit guest bedroom with an iron bed"></div>
<p class="abs body-copy intro">Welcome to the Wiesenkrone in beautiful Lindental. With great attention to detail, we have turned our old farm into a place of rest and relaxation. Whether in the tiny house "Amber" or the holiday apartments "Abendrot" and "Morgenrot", in all of our accommodations we attach great importance to the fact that you as a guest immediately feel comfortable and that you arrive in the middle of an enchanted garden and in your time-out.</p>
<div class="abs rating">
  <div class="mini"><span></span>Wiesenkrone</div>
  <div class="score">4.8</div>
  <div class="stars">★★★★★</div>
  <div class="cta">Contact Us</div>
</div>
<div class="photo" style="left:577px;top:1350px;width:188px;height:190px;border-radius:0;background:linear-gradient(135deg,#5a3418,#c9843c 60%,#7a4a22)" role="img" aria-label="Photo of the hosts at a candle-lit table"></div>
<p class="abs body-copy aside">In a quiet and idyllic location, you can still quickly reach the harbour towns of Altmarkt and Hafenstedt as well as the beaches of Seewinkel, Dünenbucht and Kliffort.</p>
<div class="abs signoff">WE LOOK FORWARD TO YOUR VISIT.</div>
<div class="abs signature">Mira &amp; Jonas</div>

<!-- Domicile -->
<div class="abs domicile"></div>
<div class="abs sec-script script" style="top:1692px">Welcome to the</div>
<h2 class="abs sec-title caps" style="top:1745px">Your Domicile</h2>

<div class="card" style="left:210px;top:1830px">
  <div class="photo" style="inset:0;background:linear-gradient(135deg,#a0652a,#e2b25c 55%,#7a5a2a)" role="img" aria-label="Photo of the Abendrot apartment living room"></div>
  <div class="glass" style="top:42px"><h3>Design Refuge "Abendrot"</h3><p>Historical elements with contemporary design characterize this feel-good loft.</p><span class="more">Learn More</span></div>
</div>
<div class="card" style="left:612px;top:1830px">
  <div class="photo" style="inset:0;background:linear-gradient(135deg,#6e4a2a,#b98a58 55%,#4e3a2a)" role="img" aria-label="Photo of the Morgenrot apartment bedroom"></div>
  <div class="glass" style="top:56px"><h3>Design Refuge "Morgenrot"</h3><p>Morgenrot shows the love for clear but warm simplicity.</p><span class="more">Learn More</span></div>
</div>
<div class="card" style="left:210px;top:2160px">
  <div class="photo" style="inset:0;background:linear-gradient(135deg,#7a5418,#d9a93a 55%,#5a3a16)" role="img" aria-label="Photo of the Silbermond tiny house interior"></div>
  <div class="glass" style="top:40px"><h3>Tiny House "Silbermond"</h3><p>Silbermond is all about modern, cozy comfort.</p><span class="more">Learn More</span></div>
</div>
<div class="card" style="left:612px;top:2160px">
  <div class="photo" style="inset:0;background:linear-gradient(135deg,#8f8a82,#d8d2c6 55%,#7a7470)" role="img" aria-label="Photo of the Birkenhaus tiny house bedroom"></div>
  <div class="glass" style="top:20px"><h3>Tiny House "Birkenhaus"</h3><p>Historical elements with contemporary design characterize this feel-good loft.</p><span class="more">Learn More</span></div>
</div>

<!-- Features -->
<div class="abs features"></div>
<div class="abs sec-script" style="top:2588px;font-family:'Great Vibes',cursive;font-size:42px;color:#fff">Features</div>
<h2 class="abs sec-title caps" style="top:2637px">Urlaub auf dem Features</h2>

<div class="feat" style="left:210px"><svg viewBox="0 0 26 22"><path d="M3 8a14 14 0 0 1 20 0M6.5 11.5a9 9 0 0 1 13 0M10 15a4 4 0 0 1 6 0" fill="none" stroke="#D89A22" stroke-width="2" stroke-linecap="round"/><circle cx="13" cy="18.5" r="1.8" fill="#D89A22"/></svg><div>Free Wifi</div></div>
<div class="feat" style="left:344px"><svg viewBox="0 0 26 22"><path d="M4 9h14v4a5 5 0 0 1-5 5H9a5 5 0 0 1-5-5z" fill="#D89A22"/><path d="M18 10h2a2.5 2.5 0 0 1 0 5h-2" fill="none" stroke="#D89A22" stroke-width="2"/><path d="M8 3v3M12 2v4" stroke="#D89A22" stroke-width="1.6"/></svg><div>Breakfast</div></div>
<div class="feat" style="left:478px"><svg viewBox="0 0 26 22"><rect x="2" y="7" width="4" height="8" fill="#D89A22"/><rect x="20" y="7" width="4" height="8" fill="#D89A22"/><rect x="6" y="10" width="14" height="2" fill="#D89A22"/></svg><div>Gym Center</div></div>
<div class="feat" style="left:611px"><svg viewBox="0 0 26 22"><path d="M5 11l2.5-6h11L21 11v6H5z" fill="#D89A22"/><circle cx="8.5" cy="14" r="1.5" fill="#fff"/><circle cx="17.5" cy="14" r="1.5" fill="#fff"/></svg><div>Parking</div></div>
<div class="feat" style="left:745px"><svg viewBox="0 0 26 22"><rect x="2" y="6" width="22" height="11" rx="5" fill="#D89A22"/><path d="M7 9v5M4.5 11.5h5" stroke="#fff" stroke-width="1.6"/><circle cx="18" cy="10" r="1.3" fill="#fff"/><circle cx="20" cy="13" r="1.3" fill="#fff"/></svg><div>Gaming Zone</div></div>
<div class="feat" style="left:878px"><svg viewBox="0 0 26 22"><path d="M2 15c3-2 5 2 8 0s5 2 8 0 5 2 6 0M2 19c3-2 5 2 8 0s5 2 8 0 5 2 6 0" fill="none" stroke="#D89A22" stroke-width="1.6"/><circle cx="17" cy="6" r="2" fill="#D89A22"/><path d="M6 12l6-5 3 4" fill="none" stroke="#D89A22" stroke-width="2"/></svg><div>Swiming Pool</div></div>

<div class="abs video" role="img" aria-label="Video still of lounge chairs and a garden seating area on the lawn"></div>
<div class="abs play"><span><svg width="26" height="28" viewBox="0 0 26 28"><path d="M4 2l20 12L4 26z" fill="none" stroke="#E9B53A" stroke-width="2.5" stroke-linejoin="round"/></svg></span></div>

<!-- Seasons -->
<div class="abs sec-script script" style="top:3376px">Seasons</div>
<h2 class="abs sec-title caps" style="top:3424px">See Our Seasons</h2>
<div class="abs tabs"><div class="on">Spring</div><div>Summer</div><div>Fall</div><div>Winter</div></div>

<div class="photo" style="left:210px;top:3600px;width:240px;height:325px;background:linear-gradient(160deg,#5a7a3a,#d9a44a 50%,#6e8a42)" role="img" aria-label="Photo of the yellow farmhouse in spring"></div>
<div class="photo" style="left:480px;top:3600px;width:240px;height:325px;background:linear-gradient(180deg,#e8ddc6,#b8b8b0 55%,#5e7a3e)" role="img" aria-label="Photo of a tiny house with wooden steps"></div>
<div class="photo" style="left:750px;top:3600px;width:240px;height:325px;background:linear-gradient(180deg,#1c3a8a,#3a5ab0 60%,#0e1a3a)" role="img" aria-label="Photo of the farm at dusk under a blue night sky"></div>
<div class="photo" style="left:210px;top:3950px;width:378px;height:208px;background:linear-gradient(135deg,#3a2416,#8a5a34 55%,#d8d0c6)" role="img" aria-label="Photo of relaxing by the stove indoors"></div>
<div class="photo" style="left:612px;top:3950px;width:378px;height:208px;background:linear-gradient(135deg,#6e4628,#c48a4e 55%,#5a3a22)" role="img" aria-label="Photo of a guest at a table by a brick wall"></div>

<!-- Map & Footer -->
<div class="abs map" role="img" aria-label="Map showing the location of the retreat"></div>
<div class="abs zoom">+<br>−</div>
<svg class="abs footer-wave" viewBox="0 0 1200 240" preserveAspectRatio="none">
  <path d="M0 200 C220 150 420 60 640 60 C860 60 1040 120 1200 60 L1200 240 L0 240 Z" fill="#E9B53A"/>
  <path d="M0 220 C220 170 420 78 640 78 C860 78 1040 140 1200 80 L1200 240 L0 240 Z" fill="#54432b"/>
</svg>
<div class="abs footer"></div>
<div class="abs foot-brand"><span class="dot"></span>Wiesenkrone</div>

<div class="abs foot-h" style="left:210px">Navigation</div>
<div class="abs foot-h" style="left:430px">Write Us</div>
<div class="abs foot-h" style="left:670px">Contact Form</div>

<div class="abs foot-links">Home<br>About Us<br>Accommodation<br>Booking &amp; Calendar<br>Gallery<br>Contact</div>
<div class="abs write">
  <div class="row"><span>✉</span>post@wiesenkrone-example.net</div>
  <div class="row"><span>
    <svg width="10" height="13" viewBox="0 0 10 13"><path d="M5 0a5 5 0 0 1 5 5c0 3.5-5 8-5 8S0 8.5 0 5a5 5 0 0 1 5-5z" fill="#fff"/><circle cx="5" cy="5" r="1.8" fill="#54432b"/></svg></span><span>Lindenweg 7, 10115 Feldhausen,<br>Germany</span></div>
  <div class="row gold"><span>✆</span>+49 000 555 014 20</div>
</div>

<div class="input" style="left:670px;top:5060px;width:156px;height:30px">Name</div>
<div class="input" style="left:834px;top:5060px;width:156px;height:30px">Email</div>
<div class="input" style="left:670px;top:5098px;width:320px;height:30px">Regarding</div>
<div class="input" style="left:670px;top:5136px;width:320px;height:96px">Your Message</div>
<div class="abs send">SEND</div>

<div class="abs copy">© 2022 www.wiesenkrone-example.net</div>

</body>
</html>
```